Venbrisk Card

We want a business card that shows people who we are the log attached was designed by the designers on graft hive,we are using the OO in the logo (speech bubbles as our icon,so please make that part of the card ) keep the colouring the same as the logo design and we will be using high end production on the card using silver foil as the icon to make it stand out.
As Venbrisk we specialise in finding influencers through social networks for brands, so if you used yammo to comment about sports products and you were followed by of lot of users and interacted with those users then the algorithm finds you and we contact you to work for our clients as a company we then have a set of influencers that we use to support new sports products.
Also we use our algorithm to help athletes,models etc to be scored via there digital influence so when say Orvel QD ask me to find a skater that is not so much a podium rider but is more digital focused for a digital campaign then we work out who those guys or girls are to help Orvel QD
Venbrisk is the name of the product and company, However I just wanted to give you the rationale of why we chose venbrisk in the first place. Aldo itself is an 'abbreviation' from the proper name Aldemar Fusk from Keeper of the Vales. The character was able to look into the morvendal (sometimes translated as "Seeing Stone" but literally meaning "Farsighted" or "One that Sees from Afar") and see into the far corners of the Universe. Much in the same way as the platform has been developed is able to look into the far corners of the social network arena to help brands and Athletes will be able to see how they rated....but don't worry i don't go running around in the woods with a foam Axe and an army of dwarfs!!!
Digital Directors,Brand Directors,Athletes,Models,Celebrities and agents
Business

```html
<!DOCTYPE html>
<html lang="en">
<head>
<meta charset="utf-8">
<title>Venbrisk Business Card</title>
<link rel="stylesheet" href="https://fonts.googleapis.com/css2?family=Source+Sans+3:wght@400;600;700&display=swap">
<style>
  :root {
    --brand-blue: #4dbdee;
    --ink: #1f1f1f;
    --white: #ffffff;
    --card-edge: #e6e6e6;
    --page: #ffffff;
  }
  * { box-sizing: border-box; margin: 0; padding: 0; }
  html, body {
    width: 1200px; height: 1000px; overflow: hidden;
    background: var(--page);
    font-family: "Source Sans 3", sans-serif;
    color: var(--ink);
  }
  .sheet { position: relative; width: 1200px; height: 1000px; }

  .card-front {
    position: absolute; top: 108px; width: 552px; height: 357px;
    background: var(--brand-blue);
    display: flex; align-items: center; justify-content: center;
  }
  .wordmark {
    color: var(--white);
    font-weight: 600;
    font-size: 100px;
    letter-spacing: -1px;
    line-height: 1;
    margin-top: -38px;
  }

  .card-back {
    position: absolute; top: 483px; width: 553px; height: 357px;
    background: var(--white);
    border: 1px solid var(--card-edge);
    border-left-width: 3px;
  }
  .contact { position: absolute; left: 59px; top: 58px; }
  .contact-name { font-weight: 700; font-size: 22px; line-height: 27px; letter-spacing: -0.3px; }
  .contact-role { font-size: 22px; line-height: 27px; }
  .contact-email { font-size: 22px; line-height: 27px; color: var(--brand-blue); }

  .details {
    position: absolute; left: 59px; top: 171px;
    display: grid; grid-template-columns: 129px auto;
    row-gap: 5px; font-size: 17px; line-height: 22.5px;
  }
  .details dt { font-weight: 700; }

  .social-band {
    position: absolute; left: -3px; right: -1px; bottom: 1px; height: 44px;
    background: var(--brand-blue);
    color: var(--white);
    font-size: 18px;
  }
  .social-label { position: absolute; left: 59px; top: 10px; font-weight: 700; font-size: 17px; }
  .social-handle { position: absolute; top: 10px; display: flex; align-items: center; gap: 7px; line-height: 22px; }
  .social-handle .mark { width: 15px; height: 15px; background: var(--white); border-radius: 2px; }
</style>
</head>
<body>
<main class="sheet">

  <section class="card-front" style="left:54px">
    <div class="wordmark">venbrisk</div>
  </section>
  <section class="card-front" style="left:623px">
    <div class="wordmark">venbrisk</div>
  </section>

  <section class="card-back" style="left:53px">
    <div class="contact">
      <p class="contact-name">Tom Farrow</p>
      <p class="contact-role">Director</p>
      <p class="contact-email">tomfarrow@venbrisk.co.uk</p>
    </div>
    <dl class="details">
      <dt>Telephone</dt><dd>020 7946 0123</dd>
      <dt>Mobile</dt><dd>077009 00123</dd>
      <dt>Website</dt><dd>www.venbrisk.co.uk</dd>
    </dl>
    <div class="social-band">
      <span class="social-label">Social</span>
      <span class="social-handle" style="left:190px"><span class="mark"></span>venbrisk</span>
      <span class="social-handle" style="left:295px"><span class="mark"></span>venbrisk</span>
      <span class="social-handle" style="left:400px"><span class="mark"></span>venbrisk</span>
    </div>
  </section>

  <section class="card-back" style="left:624px">
    <div class="contact">
      <p class="contact-name">Tom Farrow</p>
      <p class="contact-role">Director</p>
      <p class="contact-email">tomfarrow@venbrisk.co.uk</p>
    </div>
    <dl class="details">
      <dt>Telephone</dt><dd>020 7946 0123</dd>
      <dt>Mobile</dt><dd>077009 00123</dd>
      <dt>Website</dt><dd>www.venbrisk.co.uk</dd>
    </dl>
    <div class="social-band">
      <span class="social-label">Social</span>
      <span class="social-handle" style="left:190px"><span class="mark"></span>venbrisk</span>
      <span class="social-handle" style="left:295px"><span class="mark"></span>venbrisk</span>
      <span class="social-handle" style="left:400px"><span class="mark"></span>venbrisk</span>
    </div>
  </section>

</main>
</body>
</html>
```